Brookmere Recovery Center Billboard (Addiction / Alcohol / Opioid )

visit www.brookmererecovery-example.com
We are an inpatient treatment center for opioid, alcohol and drug addiction. We are looking to get multiple 12'x25' billboards in our area. Our Phone number is 1-855-CALM-NOW we are located in Auburn Indiana
We pride ourselves on a comfortable medical detox and treat our patients as family.

Target Market(s)

Current Addicts, Addicts family or friends, Factory Workers and Shopvane shoppers

Industry/Entity Type

Health Care

Font styles to use
Sans Serif

Colors
0355a3
3176b5
ffffff

Requirements
Must have
• Logo and Phone number, and Brookmere Recovery
Nice to have
• Ideas?
1.) Addiction hurts more than yourself. (Pic of little girl?)
2.) Just how much are you willing to lose?
3.) Addiction does not define you, You are what you choose to become.
4.) Indiana's most comfortable Detox
5.) Detox in unmatched comfort.
6.) Background could be patient room with logo in upper right
7.) Looking to be able to read easily from road.
Should not have
• Hard to read lettering

```html
<!DOCTYPE html>
<html lang="en">
<head>
<meta charset="utf-8">
<title>Brookmere Recovery Billboard</title>
<link href="https://fonts.googleapis.com/css2?family=Montserrat:wght@500;600;700;800;900&family=Oswald:wght@400&display=swap" rel="stylesheet">
<style>
  :root{
    --navy:#0b2265;
    --cyan:#12c0ec;
    --ink:#2b2b2b;
    --white:#ffffff;
    --stage:#6b6b6b;
    --room-light:#f4f4f2;
    --room-mid:#e2e0dc;
  }
  *{margin:0;padding:0;box-sizing:border-box}
  html,body{width:1000px;height:1200px;overflow:hidden}
  body{
    background:radial-gradient(ellipse at 60% 50%, #9a9a9a 0%, var(--stage) 70%, #3e3e3e 100%);
    font-family:"Montserrat", Arial, sans-serif;
    position:relative;
  }
  .billboard{
    position:absolute;left:40px;top:379px;width:920px;height:442px;
    overflow:hidden;background:var(--room-light);
    box-shadow:0 10px 28px rgba(0,0,0,.45);
  }
  .billboard-art{position:absolute;inset:0;width:920px;height:442px}
  .headline{
    position:absolute;left:38px;top:30px;color:var(--ink);line-height:1;
  }
  .headline .lead{font-weight:700;font-size:34px;letter-spacing:.5px}
  .headline .hurts{font-weight:900;font-size:70px;color:var(--navy);margin-left:8px;letter-spacing:-1px}
  .headline .more{display:block;font-weight:800;font-size:42px;margin-top:-6px}
  .headline .yourself{display:block;font-weight:900;font-size:74px;color:var(--cyan);margin-left:40px;margin-top:-10px;letter-spacing:-1.5px}
  .brand{
    position:absolute;left:40px;top:268px;display:flex;align-items:center;gap:12px;
  }
  .brand-dot{width:62px;height:62px;border-radius:50%;background:var(--navy);flex:none}
  .brand-name{font-weight:700;font-size:25px;color:var(--navy);line-height:1.1;letter-spacing:.5px}
  .web{
    position:absolute;left:37px;top:386px;font-family:"Oswald", Arial Narrow, sans-serif;
    font-size:23px;color:var(--navy);letter-spacing:-.2px;
  }
  .badge{
    position:absolute;left:289px;top:210px;width:162px;height:162px;border-radius:50%;
    background:var(--navy);border:7px solid var(--cyan);
    display:flex;flex-direction:column;align-items:center;justify-content:center;
    color:var(--white);font-size:14.5px;line-height:1.22;text-align:center;font-weight:500;
  }
  .badge b{font-weight:800}
  .phone{
    position:absolute;left:392px;top:380px;height:54px;display:flex;align-items:center;gap:18px;
    color:var(--white);
  }
  .phone svg{width:36px;height:36px;flex:none}
  .phone-number{font-weight:800;font-size:47px;letter-spacing:-.5px}
</style>
</head>
<body>
  <section class="billboard">
    <svg class="billboard-art" viewBox="0 0 920 442" aria-hidden="false">
      <defs>
        <linearGradient id="roomTone" x1="0" y1="0" x2="1" y2="1">
          <stop offset="0" stop-color="#f6f6f5"/>
          <stop offset=".6" stop-color="#ecebe8"/>
          <stop offset="1" stop-color="#dcd6ce"/>
        </linearGradient>
        <linearGradient id="photoTone" x1="0" y1="0" x2="1" y2="1">
          <stop offset="0" stop-color="#f1f0ec"/>
          <stop offset=".45" stop-color="#e2c3a2"/>
          <stop offset=".75" stop-color="#d9a983"/>
          <stop offset="1" stop-color="#ebe6df"/>
        </linearGradient>
      </defs>
      <g role="img" aria-label="Softly faded photo of a calm patient bedroom with bed and dresser">
        <rect width="920" height="442" fill="url(#roomTone)"/>
      </g>
      <g role="img" aria-label="Photo of a sad young girl sitting against a white wall hugging her knees">
        <path d="M650 0 L920 0 L920 373 L505 373 C545 330 560 250 585 160 C605 90 620 40 650 0 Z" fill="url(#photoTone)"/>
      </g>
      <path class="swoosh-navy" d="M632 0 C600 40 585 110 560 190 C530 290 480 360 400 405 C350 430 300 440 220 442" fill="none" stroke="var(--navy)" stroke-width="16"/>
      <path class="swoosh-cyan" d="M658 0 C625 40 605 110 580 195 C555 285 515 345 470 378" fill="none" stroke="var(--cyan)" stroke-width="9"/>
      <path class="phone-bar" d="M330 442 C400 425 450 400 480 373 L920 373 L920 442 Z" fill="var(--navy)"/>
    </svg>

    <h1 class="headline">
      <span class="lead">Addiction</span><span class="hurts">hurts</span>
      <span class="more">more than</span>
      <span class="yourself">yourself</span>
    </h1>

    <div class="brand">
      <span class="brand-dot"></span>
      <span class="brand-name">Brookmere<br>Recovery</span>
    </div>
    <p class="web">BrookmereRecovery-example.com</p>

    <div class="badge">
      <span>Indiana's</span>
      <b>most</b>
      <b>comfortable</b>
      <span>medical Detox</span>
      <span>located in</span>
      <b>Auburn.</b>
    </div>

    <div class="phone">
      <svg viewBox="0 0 24 24" fill="none" stroke="#ffffff" stroke-width="1.6" stroke-linecap="round" stroke-linejoin="round" aria-hidden="true">
        <path d="M22 16.9v3a2 2 0 0 1-2.2 2 19.8 19.8 0 0 1-8.6-3.1 19.5 19.5 0 0 1-6-6A19.8 19.8 0 0 1 2.1 4.2 2 2 0 0 1 4.1 2h3a2 2 0 0 1 2 1.7c.1.9.4 1.8.7 2.7a2 2 0 0 1-.5 2.1L8 9.8a16 16 0 0 0 6 6l1.3-1.3a2 2 0 0 1 2.1-.4c.9.3 1.8.6 2.7.7a2 2 0 0 1 1.7 2z"/>
        <path d="M15 2a7 7 0 0 1 7 7"/><path d="M15 6a3 3 0 0 1 3 3"/>
      </svg>
      <span class="phone-number">1-855-CALM-NOW</span>
    </div>
  </section>
</body>
</html>
```